Business card for a vending machine business

I need a business card for my vending machine business. The name is Kestrel Snackworks, LLC. The card is one-sided, and landscape format. Not portrait.

The information for the card is as follows:

Dana Whitlow
Owner
(555) 314-2907
Kestrelsnackworks.example
Info@kestrelsnackworks.example

I'd like colors and design elements to match what's in my logo and company name. I'd like to have the checkered flag or racing stripe if possible You can use a border if youd like. You can use a background color if it looks nice and doesn't clash with the logo
Use your creativity. But a white background is perfectly fine. The card can be as simple, yet gets the point across to match the company name and logo.

I uploaded a copy of my logo. I also uploaded a businesses card I started to create, but since it was missing something, I gave up. Another upload has a red thunderbolt and the checkerer flag. Those two uploads are for inspiration. Again, please make sure to make the card landscape, not portrait. Thank you, designers. Good luck to all.

```html
<!DOCTYPE html>
<html lang="en">
<head>
<meta charset="utf-8">
<title>Kestrel Snackworks — Business Card</title>
<link rel="stylesheet" href="https://fonts.googleapis.com/css2?family=Poppins:wght@400;500;600;800&display=swap">
<style>
  :root {
    --navy: #1d3577;
    --navy-deep: #0f1d52;
    --navy-text: #15245a;
    --red: #e4202b;
    --white: #ffffff;
    --paper: #f4f3f8;
    --stage: #e6e6ec;
  }
  * { box-sizing: border-box; margin: 0; padding: 0; }
  html, body {
    width: 1200px; height: 789px; overflow: hidden;
    background: var(--stage);
    font-family: "Poppins", sans-serif;
  }
  .stage { position: relative; width: 1200px; height: 789px; }
  .card {
    position: absolute; top: 240px;
    width: 540px; height: 309px;
    border-radius: 22px; overflow: hidden;
    box-shadow: 0 6px 18px rgba(20, 25, 60, 0.18);
  }
  .card--front { left: 40px; }
  .card--back { left: 620px; background: linear-gradient(160deg, var(--navy) 0%, var(--navy-deep) 100%); }
  .card__shape { position: absolute; inset: 0; }

  .brand-mark {
    position: absolute; left: 18px; top: 112px; width: 200px;
    display: flex; flex-direction: column; align-items: center; gap: 8px;
    color: var(--white); font-weight: 800; text-align: center;
    font-size: 22px; line-height: 1.1; text-transform: uppercase;
  }
  .brand-mark__dot { width: 14px; height: 14px; border-radius: 50%; background: var(--red); }

  .contact-block { position: absolute; left: 262px; top: 52px; color: var(--navy-text); }
  .contact-block__name { font-size: 27px; font-weight: 800; letter-spacing: 0.5px; line-height: 1.1; }
  .contact-block__role { font-size: 20px; font-weight: 400; margin-top: 2px; }
  .contact-list { list-style: none; margin-top: 22px; display: flex; flex-direction: column; gap: 10px; }
  .contact-list__item { display: flex; align-items: center; gap: 10px; font-size: 12.5px; font-weight: 400; }
  .contact-list__icon {
    width: 26px; height: 26px; flex: none; border: 2px solid var(--navy-text); border-radius: 50%;
    display: flex; align-items: center; justify-content: center;
  }

  .back-brand {
    position: absolute; left: 0; right: 0; top: 104px;
    display: flex; align-items: center; justify-content: center; gap: 12px;
    color: var(--white); font-weight: 800; font-size: 32px; text-transform: uppercase;
  }
  .back-brand__square { width: 16px; height: 16px; background: var(--red); }
  .back-rule { position: absolute; left: 150px; right: 150px; top: 170px; height: 4px; background: var(--red); }
  .tagline {
    position: absolute; left: 0; right: 0; top: 188px; text-align: center;
    color: var(--white); font-weight: 600; font-size: 16px;
  }
</style>
</head>
<body>
<main class="stage">
  <section class="card card--front" aria-label="Business card front">
    <svg class="card__shape" viewBox="0 0 540 309" preserveAspectRatio="none" aria-hidden="true">
      <defs>
        <linearGradient id="paper-fill" x1="0" y1="0" x2="1" y2="1">
          <stop offset="0" stop-color="#ffffff"/>
          <stop offset="1" stop-color="#eeedf4"/>
        </linearGradient>
        <linearGradient id="navy-fill" x1="0" y1="0" x2="0.6" y2="1">
          <stop offset="0" stop-color="#23408a"/>
          <stop offset="1" stop-color="#18306d"/>
        </linearGradient>
      </defs>
      <rect width="540" height="309" fill="url(#paper-fill)"/>
      <polygon points="0,0 196,0 250,309 0,309" fill="url(#navy-fill)"/>
      <line x1="196" y1="0" x2="250" y2="309" stroke="#e4202b" stroke-width="5"/>
    </svg>

    <div class="brand-mark">
      <span class="brand-mark__dot"></span>
      <span>Kestrel Snackworks</span>
    </div>

    <div class="contact-block">
      <p class="contact-block__name">DANA WHITLOW</p>
      <p class="contact-block__role">Owner</p>
      <ul class="contact-list">
        <li class="contact-list__item">
          <span class="contact-list__icon">
            <svg width="12" height="12" viewBox="0 0 24 24" aria-hidden="true"><path d="M6.6 10.8a15 15 0 0 0 6.6 6.6l2.2-2.2a1 1 0 0 1 1-.25 11.4 11.4 0 0 0 3.6.6 1 1 0 0 1 1 1V20a1 1 0 0 1-1 1A17 17 0 0 1 3 4a1 1 0 0 1 1-1h3.5a1 1 0 0 1 1 1c0 1.25.2 2.45.6 3.6a1 1 0 0 1-.25 1z" fill="#15245a"/></svg>
          </span>
          <span>(555) 314-2907</span>
        </li>
        <li class="contact-list__item">
          <span class="contact-list__icon">
            <svg width="12" height="12" viewBox="0 0 24 24" aria-hidden="true"><rect x="2" y="5" width="20" height="14" rx="2" fill="#15245a"/><path d="M3 6l9 7 9-7" stroke="#fff" stroke-width="1.8" fill="none"/></svg>
          </span>
          <span>Info@kestrelsnackworks.example</span>
        </li>
        <li class="contact-list__item">
          <span class="contact-list__icon">
            <svg width="11" height="11" viewBox="0 0 24 24" aria-hidden="true"><path d="M4 3l16 7-7 2-2 7z" fill="#15245a"/></svg>
          </span>
          <span>Kestrelsnackworks.example</span>
        </li>
      </ul>
    </div>
  </section>

  <section class="card card--back" aria-label="Business card back">
    <div class="back-brand">
      <span class="back-brand__square"></span>
      <span>Kestrel Snackworks</span>
    </div>
    <div class="back-rule"></div>
    <p class="tagline">Fresh Picks, Quick Stops, Every Single Day</p>
  </section>
</main>
</body>
</html>
```